My Insurance Agency Show Display

I need to design a 10 ft x 8 ft backdrop for a show display. This is a pop up fabric most likely display that will be used for a show booth. I need someone to design something more attractive with my logo and make it more flashy so people can see and remember my company. I have attached my rough design so far. I would like it to look more modern. The photo in the design does not have to be used.

This is for an insurance agency that provides Home, Auto, Life and Health products to consumers. We also provide Renters insurance, Commercial, RV, mobile homes, and other products to our customers.

Target Market(s)

Home Owners, and Multiple Auto Owners

Industry/Entity Type

Property and Causality Insurance

Font styles to use
Sans Serif

Colors
0054AA
0677BA
7BADD7
CADEEF
E8F1F8
00AB8E
00BBA5
67D7C9
C6EFE9
E9F9F6

Requirements
Must have
• Attractive Modern Layout
Nice to have
• new and creative. Something that pops with color
Should not have
• Any affiliation to other insurance agencies.

```html
<!DOCTYPE html>
<html lang="en">
<head>
<meta charset="utf-8">
<title>Harborline Insurance Agency – Show Backdrop</title>
<link href="https://fonts.googleapis.com/css2?family=Montserrat:wght@400;700;800&family=Fira+Sans:wght@600&display=swap" rel="stylesheet">
<style>
  :root {
    --white: #ffffff;
    --magenta: #d81d5c;
    --blush: #f4c6d6;
    --navy: #0d2340;
    --ink: #1d1d1f;
    --teal: #00ab8e;
    --teal-bright: #1cd9c4;
    --mint-text: #c6effa;
    --shadow-grey: #c9ced1;
    --blue: #0054aa;
    --photo-light: #e6dccb;
    --photo-mid: #b89a78;
    --photo-dark: #5e4a3a;
  }
  * { box-sizing: border-box; margin: 0; padding: 0; }
  html, body { width: 1200px; height: 960px; overflow: hidden; background: var(--white); }
  .backdrop {
    position: relative;
    width: 1200px;
    height: 960px;
    overflow: hidden;
    background: var(--white);
    font-family: "Montserrat", sans-serif;
  }

  /* Brand block */
  .brand { position: absolute; left: 117px; top: 44px; width: 330px; text-align: center; }
  .brand-square {
    width: 84px; height: 84px; margin: 0 auto 30px;
    background: var(--magenta);
  }
  .brand-name {
    font-family: "Montserrat", sans-serif;
    font-weight: 800;
    color: var(--ink);
    font-size: 34px;
    line-height: 1.05;
    letter-spacing: 1px;
  }
  .brand-name .brand-sub { display: block; font-size: 27px; letter-spacing: 7px; margin-top: 8px; }

  /* Hero photo area */
  .hero-photo {
    position: absolute; left: 584px; top: 0; width: 573px; height: 365px;
    background: linear-gradient(135deg, var(--photo-light) 0%, var(--photo-mid) 55%, var(--photo-dark) 100%);
  }
  .hero-accent { position: absolute; left: 1157px; top: 0; width: 43px; height: 365px; background: var(--magenta); }

  /* Decorative faint shape */
  .deco-shape { position: absolute; left: 757px; top: 400px; width: 446px; height: 446px; }

  /* Product menu */
  .product-menu { position: absolute; left: 39px; top: 335px; list-style: none; }
  .product-menu li {
    position: relative;
    width: 205px; height: 49px;
    background: var(--teal);
    border-radius: 6px;
    box-shadow: 0 4px 0 var(--shadow-grey);
    overflow: hidden;
  }
  .product-menu li::after {
    content: ""; position: absolute; right: 0; top: 0; width: 22px; height: 100%;
    background: var(--teal-bright);
  }
  .product-menu .item-label {
    position: absolute; right: 31px; top: 0; line-height: 49px;
    font-family: "Fira Sans", sans-serif; font-weight: 600;
    font-size: 23px; color: var(--mint-text);
  }
  .product-menu li + li { margin-top: 11px; }

  /* Headline + copy */
  .headline {
    position: absolute; left: 284px; top: 474px;
    font-weight: 800; font-size: 78px; line-height: 1;
    color: var(--magenta); letter-spacing: -1px;
  }
  .subhead {
    position: absolute; left: 285px; top: 567px;
    font-weight: 800; font-size: 35.5px; line-height: 1;
    color: var(--navy); letter-spacing: 0.5px;
  }
  .intro {
    position: absolute; left: 290px; top: 606px; width: 600px;
    font-weight: 400; font-size: 19px; line-height: 30.6px;
    color: var(--ink);
  }

  /* Contact bar */
  .contact-bar { position: absolute; left: 0; top: 894px; width: 1200px; height: 66px; background: var(--blue); }
  .contact-icon { position: absolute; }
  .icon-mail { left: 64px; top: 13px; }
  .icon-phone { left: 472px; top: 8px; }
  .icon-pin { left: 858px; top: 7px; }
</style>
</head>
<body>
<div class="backdrop">

  <div class="brand">
    <div class="brand-square"></div>
    <div class="brand-name">HARBORLINE<span class="brand-sub">INSURANCE AGENCY</span></div>
  </div>

  <div class="hero-photo" role="img" aria-label="Photo of a smiling family of four cuddling together on a sofa"></div>
  <div class="hero-accent"></div>

  <svg class="deco-shape" viewBox="0 0 446 446" aria-hidden="true">
    <circle cx="223" cy="223" r="220" fill="var(--blush)" opacity="0.8"/>
  </svg>

  <ul class="product-menu">
    <li><span class="item-label">Home</span></li>
    <li><span class="item-label">Auto</span></li>
    <li><span class="item-label">Life</span></li>
    <li><span class="item-label">Health</span></li>
    <li><span class="item-label">Umbrella</span></li>
    <li><span class="item-label">Renters</span></li>
    <li><span class="item-label">Insurance</span></li>
    <li><span class="item-label">Commercial</span></li>
    <li><span class="item-label">Mobile homes</span></li>
  </ul>

  <h1 class="headline">PROTECTING</h1>
  <h2 class="subhead">WHAT MATTERS MOST TO YOU</h2>
  <p class="intro">Our comprehensive insurance services provide you with peace of mind, ensuring that your assets, health, and loved ones are safeguarded against unforeseen circumstances. Trust in our expertise to navigate the complexities of insurance and secure a brighter future for you and your family.</p>

  <div class="contact-bar">
    <svg class="contact-icon icon-mail" width="60" height="41" viewBox="0 0 60 41" aria-label="Email">
      <rect x="1.5" y="1.5" width="57" height="38" fill="none" stroke="var(--white)" stroke-width="2.5"/>
      <polyline points="2,2 30,24 58,2" fill="none" stroke="var(--white)" stroke-width="2.5"/>
      <line x1="2" y1="39" x2="22" y2="18" stroke="var(--white)" stroke-width="2.5"/>
      <line x1="58" y1="39" x2="38" y2="18" stroke="var(--white)" stroke-width="2.5"/>
    </svg>
    <svg class="contact-icon icon-phone" width="52" height="52" viewBox="0 0 24 24" aria-label="Phone">
      <path d="M6.6 2.5c.6-.5 1.5-.4 2 .2l2 2.7c.4.6.4 1.4-.1 1.9l-1.3 1.3c.9 2 2.6 3.8 4.6 4.8l1.3-1.3c.5-.5 1.3-.6 1.9-.1l2.7 2c.6.5.7 1.4.2 2l-1.4 1.7c-.8 1-2.2 1.3-3.4.8C10.7 17.1 6.9 13.3 5.4 8.9c-.4-1.2-.1-2.5.8-3.4z" fill="none" stroke="var(--white)" stroke-width="1.1" stroke-linejoin="round"/>
    </svg>
    <svg class="contact-icon icon-pin" width="40" height="52" viewBox="0 0 40 52" aria-label="Location">
      <path d="M20 50 C10 36 3 28 3 19 A17 17 0 0 1 37 19 C37 28 30 36 20 50 Z" fill="none" stroke="var(--white)" stroke-width="2.6" stroke-linejoin="round"/>
      <circle cx="20" cy="19" r="7" fill="none" stroke="var(--white)" stroke-width="2.6"/>
    </svg>
  </div>

</div>
</body>
</html>
```